Country House in Italy Needs a Business Card Design

We need a business card design for “Casale del Ruscello”, a modern concept of a Farm Holidays/Country House to be opened in central Italy.
Attached is the company logo you did for us in the past.
Please
- create a double-sided business card design
- on the back I would like to have the logo
- on the front the copy
Copy on card:
o Casale del Ruscello
o Address: Via Fontalba, 14
Valdiruscio (VR), Italy
o Website: www.casaledelruscello.it
o Email: info@casaledelruscello.it
o my name : Lucilla
o my mobile phone number: +39 347 8124591
In the distribution of information keep in mind the possible inclusion also of a landline telephone number (currently not available / existing).
WE WOULD LIKE TO HAVE A MODERN, PROFFESIONAL, OUT OF THE BOX BUSINESS CARD. BE AS CREATIVE AS YOU WOULD LIKE.

```html
<!DOCTYPE html>
<html lang="it">
<head>
<meta charset="utf-8">
<title>Casale del Ruscello – Business Card</title>
<link rel="stylesheet" href="https://fonts.googleapis.com/css2?family=Libre+Baskerville:wght@700&family=Open+Sans:wght@400;600&display=swap">
<style>
  :root {
    --backdrop: #232323;
    --card-white: #fbfbfb;
    --card-grey: #ececec;
    --glow-orange: #f2a33a;
    --glow-amber: #c98a3e;
    --brand-brown: #5a3a22;
    --tagline-orange: #e0822e;
    --accent-red: #d4461e;
    --icon-orange: #d9531e;
    --text-dark: #2e2e2e;
    --text-mid: #555555;
    --mark-fill: #dc9a62;
    --disc-tint: rgba(232, 180, 140, 0.28);
  }
  * { margin: 0; padding: 0; box-sizing: border-box; }
  html, body { width: 1200px; height: 900px; overflow: hidden; }
  body {
    background: var(--backdrop);
    position: relative;
    font-family: "Open Sans", Arial, sans-serif;
  }
  .card {
    position: absolute;
    left: 280px;
    width: 640px;
    height: 366px;
    border-radius: 22px;
    overflow: hidden;
    background:
      radial-gradient(circle at 0% 0%, var(--glow-orange) 0%, rgba(242,163,58,0.45) 14%, rgba(242,163,58,0) 38%),
      radial-gradient(circle at 100% 100%, var(--glow-amber) 0%, rgba(201,138,62,0.35) 12%, rgba(201,138,62,0) 32%),
      linear-gradient(160deg, var(--card-white) 0%, var(--card-grey) 100%);
    box-shadow: 0 14px 30px rgba(0,0,0,0.55);
  }
  .card--back { top: 52px; }
  .card--front { top: 482px; }

  .brand-name {
    font-family: "Libre Baskerville", Georgia, serif;
    font-weight: 700;
    color: var(--brand-brown);
    letter-spacing: -0.5px;
    white-space: nowrap;
  }
  .brand-tagline {
    font-family: "Open Sans", Arial, sans-serif;
    font-weight: 400;
    color: var(--tagline-orange);
    letter-spacing: 0.5px;
    white-space: nowrap;
  }

  /* back side */
  .brand-disc {
    position: absolute;
    right: 64px;
    top: 40px;
    width: 200px;
    height: 200px;
    border-radius: 50%;
    background: var(--mark-fill);
  }
  .brand-back {
    position: absolute;
    left: 56px;
    top: 232px;
  }
  .brand-back .brand-name { font-size: 32px; }
  .brand-back .brand-tagline { font-size: 18px; margin: 2px 0 0 150px; }

  /* front side */
  .brand-front {
    position: absolute;
    left: 36px;
    top: 104px;
  }
  .brand-front .brand-name { font-size: 25px; }
  .brand-front .brand-tagline { font-size: 15px; margin: 1px 0 0 80px; }

  .contact {
    position: absolute;
    right: 24px;
    top: 44px;
    width: 300px;
    text-align: center;
  }
  .contact-disc {
    position: absolute;
    left: 50%;
    top: 50%;
    width: 230px;
    height: 230px;
    margin: -112px 0 0 -115px;
    border-radius: 50%;
    background: var(--disc-tint);
  }
  .contact-name {
    position: relative;
    color: var(--accent-red);
    font-weight: 600;
    font-size: 18px;
    letter-spacing: 0.5px;
  }
  .contact-address {
    position: relative;
    color: var(--text-mid);
    font-size: 13px;
    margin-bottom: 12px;
    white-space: nowrap;
  }
  .contact-list {
    position: relative;
    list-style: none;
    text-align: left;
    padding-left: 44px;
  }
  .contact-item {
    display: flex;
    align-items: center;
    gap: 12px;
    font-size: 15px;
    color: var(--text-dark);
    margin-bottom: 10px;
    white-space: nowrap;
  }
  .contact-icon {
    width: 24px;
    height: 24px;
    border-radius: 50%;
    background: var(--icon-orange);
    display: flex;
    align-items: center;
    justify-content: center;
    flex-shrink: 0;
  }
  .contact-icon svg { width: 14px; height: 14px; }
</style>
</head>
<body>
  <section class="card card--back" aria-label="Card back">
    <div class="brand-disc" aria-hidden="true"></div>
    <div class="brand-back">
      <h1 class="brand-name">Casale del Ruscello</h1>
      <p class="brand-tagline">COUNTRY HOUSE</p>
    </div>
  </section>

  <section class="card card--front" aria-label="Card front">
    <div class="brand-front">
      <h2 class="brand-name">Casale del Ruscello</h2>
      <p class="brand-tagline">COUNTRY HOUSE</p>
    </div>
    <div class="contact">
      <div class="contact-disc" aria-hidden="true"></div>
      <p class="contact-name">LUCILLA</p>
      <p class="contact-address">Via Fontalba, 14 Valdiruscio (VR), Italy</p>
      <ul class="contact-list">
        <li class="contact-item">
          <span class="contact-icon"><svg viewBox="0 0 14 14"><rect x="4" y="1.5" width="6" height="11" rx="1" fill="none" stroke="#111" stroke-width="1.4"/><circle cx="7" cy="10.5" r="0.8" fill="#111"/></svg></span>
          +39 347 8124591
        </li>
        <li class="contact-item">
          <span class="contact-icon"><svg viewBox="0 0 14 14"><circle cx="7" cy="7" r="5.5" fill="none" stroke="#111" stroke-width="1.2"/><ellipse cx="7" cy="7" rx="2.4" ry="5.5" fill="none" stroke="#111" stroke-width="1"/><line x1="1.5" y1="7" x2="12.5" y2="7" stroke="#111" stroke-width="1"/></svg></span>
          www.casaledelruscello.it
        </li>
        <li class="contact-item">
          <span class="contact-icon"><svg viewBox="0 0 14 14"><rect x="2" y="3.5" width="10" height="7" fill="none" stroke="#111" stroke-width="1.2"/><polyline points="2,3.5 7,8 12,3.5" fill="none" stroke="#111" stroke-width="1.2"/></svg></span>
          info@casaledelruscello.it
        </li>
        <li class="contact-item">
          <span class="contact-icon"><svg viewBox="0 0 14 14"><path d="M3 2.5 L5.2 2.5 L6 5 L4.6 6 C5.3 7.6 6.4 8.7 8 9.4 L9 8 L11.5 8.8 L11.5 11 C7 11.5 2.5 7 3 2.5 Z" fill="#111"/></svg></span>
          +39 0733 604218
        </li>
      </ul>
    </div>
  </section>
</body>
</html>
```